Tabletop Sign for Support Coordination Service

We need a design for a table top sign for a Support Coordination enterprise. We find and coordinate support services for those with various disabilities. We would like designs that incorporate our logo and colors, blues and greens as seen in the file upload. Additionally, we would also preferably like designs with a more modern feel. The final design should include all these in addition to our contact information (email and telephone).

```html
<!DOCTYPE html>
<html lang="en">
<head>
<meta charset="utf-8">
<title>Verda Support Services – Tabletop Sign</title>
<link rel="stylesheet" href="https://fonts.googleapis.com/css2?family=Exo+2:wght@500;600;700&display=swap">
<style>
  :root {
    --page-bg: #eef0f1;
    --brand-green: #5cc23a;
    --brand-blue: #0d4f86;
    --band-navy: #0b3f5e;
    --meadow: #3f9a3a;
    --white: #ffffff;
  }
  * { box-sizing: border-box; margin: 0; padding: 0; }
  html, body {
    width: 1200px; height: 593px; overflow: hidden;
    background: var(--page-bg);
    font-family: "Exo 2", sans-serif;
  }
  .sign {
    position: absolute; left: 422px; top: 16px;
    width: 356px; height: 561px; overflow: hidden;
    background: linear-gradient(180deg, #ffffff 0%, #f3f8ee 20%, #9ccd7e 45%, #46a83c 65%, #1f7a58 80%, var(--brand-blue) 100%);
    box-shadow: 0 6px 18px rgba(0,0,0,0.15);
  }
  .sign__photo {
    position: absolute; left: 0; top: 22px; width: 240px; height: 420px;
    background: linear-gradient(180deg, rgba(200,220,170,0.7) 0%, rgba(120,170,90,0.75) 40%, rgba(60,140,60,0.6) 75%, rgba(40,120,80,0) 100%);
    border-radius: 0 0 60px 0;
  }
  .brand-name {
    position: absolute; right: 13px; top: 104px;
    font-weight: 700; font-size: 44px; line-height: 1; letter-spacing: 1px;
    color: var(--brand-green);
  }
  .title-band {
    position: absolute; left: 139px; right: 0; top: 184px; height: 109px;
    background: var(--band-navy);
    padding: 7px 14px 0 0; text-align: right;
    color: var(--white); font-weight: 600; font-size: 28px; line-height: 33px;
  }
  .services {
    position: absolute; right: 12px; top: 322px; width: 180px;
    list-style: none; color: var(--white); font-weight: 500; font-size: 15px; line-height: 16px; text-align: right;
  }
  .services__item { display: flex; justify-content: flex-end; align-items: flex-start; gap: 6px; padding: 6px 0; }
  .services__item + .services__item { border-top: 1px dotted rgba(255,255,255,0.8); padding-top: 12px; }
  .services__tick { flex: none; margin-top: 2px; }
  .phone {
    position: absolute; left: 26px; top: 434px;
    font-weight: 700; font-size: 45px; line-height: 1; letter-spacing: 0.5px;
    color: var(--brand-green);
  }
  .web {
    position: absolute; left: 29px; top: 487px; width: 292px; height: 30px;
    background: var(--white); color: var(--brand-blue);
    font-weight: 600; font-size: 12px; letter-spacing: 2.2px;
    display: flex; align-items: center; justify-content: center;
  }
</style>
</head>
<body>
  <main class="sign">
    <div class="sign__photo" role="img" aria-label="Photo of a smiling caregiver with an older man in a wheelchair on a sunny garden path"></div>
    <div class="brand-name">VERDA</div>
    <h1 class="title-band">VERDA<br>SUPPORT<br>SERVICES</h1>
    <ul class="services">
      <li class="services__item">
        <span>Support<br>Coordination</span>
        <svg class="services__tick" width="13" height="13" viewBox="0 0 13 13"><circle cx="6.5" cy="6.5" r="6.5" fill="#fff"/><path d="M3.5 6.8l2 2 4-4.3" stroke="#3f9a3a" stroke-width="1.8" fill="none" stroke-linecap="round" stroke-linejoin="round"/></svg>
      </li>
      <li class="services__item">
        <span>Navigating Abilities<br>Together</span>
        <svg class="services__tick" width="13" height="13" viewBox="0 0 13 13"><circle cx="6.5" cy="6.5" r="6.5" fill="#fff"/><path d="M3.5 6.8l2 2 4-4.3" stroke="#3f9a3a" stroke-width="1.8" fill="none" stroke-linecap="round" stroke-linejoin="round"/></svg>
      </li>
    </ul>
    <div class="phone">(555)-214-0381</div>
    <div class="web">www.verdasupportservices.com</div>
  </main>
</body>
</html>
```